Website for company called VORENTbio

We need a website for our new company called VORENTbio which developed a platform/technology to identify antigen-specific T cells (immune cells) which can be used for cancer therapy, autoimmunity, etc.

The platform is called VORENT and is rapid, versatile, unbiased, and inexpensive.

We have a semi-final logo although we are not completely set on color and font of text (attached).

Target Market(s)

Our target audience at the moment would be potential investors and VCs. We eventually are interested in getting attention from scientists and cell/immunotherapy companies.

Industry/Entity Type

Healthcare/Technology

Coding

Coded - Design and coding required

Number of Pages Required

1 page

Colors
0094D4
00A9DD
6FCCEA
C7EBF8
E9F6FB
00AB8E
00BBA5
67D7C9
C6EFE9
E9F9F6
E54698
E96AAD
F1A4CE
F9D9EA
FCEFF6
A7469A
B969AE
D3A5CF
EDDBEB
F8F0F9
6B429C
8869AF
B7A5CE
E3DAEB
F3F0F8

Requirements
Must have
• Landing page about the company, About us page, Technology page (could be merged with company landing page), Contact us page

```html
<!DOCTYPE html>
<html lang="en">
<head>
<meta charset="utf-8">
<title>VORENTbio</title>
<link rel="stylesheet" href="https://fonts.googleapis.com/css2?family=Audiowide&family=Exo+2:wght@400;500;600&display=swap">
<style>
:root{
  --bg:#03050f;
  --bg-deep:#02030a;
  --ink:#ffffff;
  --lilac:#cfa8f3;
  --nav-active:#7fb4ea;
  --btn-a:#b04aa0;
  --btn-b:#7a4aa8;
  --field:#000000;
  --field-line:#3a3f52;
  --rule:#1a1d2a;
  --icon:#a7469a;
}
*{margin:0;padding:0;box-sizing:border-box}
html,body{width:1200px;height:3266px;overflow:hidden;background:var(--bg)}
body{font-family:"Exo 2",sans-serif;color:var(--ink);position:relative}
.abs{position:absolute}
.display{font-family:"Audiowide",sans-serif;font-weight:400}
.lilac{color:var(--lilac)}
.btn{position:absolute;display:flex;align-items:center;justify-content:center;background:linear-gradient(90deg,var(--btn-a),var(--btn-b));color:#fff;font-weight:600;font-size:16px;text-transform:uppercase;letter-spacing:.2px}

.nav{position:absolute;left:0;width:1200px;height:104px}
.brand{position:absolute;left:112px;top:24px;display:flex;align-items:center;gap:12px;font-family:"Exo 2",sans-serif;font-weight:600;font-size:44px;color:#fff}
.brand .dot{width:22px;height:22px;border-radius:50%;background:#fff}
.nav-links{position:absolute;left:607px;top:42px;display:flex;gap:34px;font-weight:500;font-size:16px;text-transform:uppercase}
.nav-links .active{color:var(--nav-active)}
.nav .btn{left:942px;top:30px;width:146px;height:45px}

.hero{position:absolute;left:0;top:0;width:1200px;height:725px;background:radial-gradient(ellipse 360px 330px at 880px 330px,#3a2550 0%,#1b2540 45%,transparent 75%),radial-gradient(ellipse 400px 300px at 150px 350px,#15263e 0%,transparent 70%),linear-gradient(180deg,#0c1628,#0a1a2c)}
.hero-title{position:absolute;left:112px;top:180px;font-size:50px;line-height:57px}
.hero-sub{position:absolute;left:112px;top:384px;width:640px;font-size:19px;line-height:33.5px;font-weight:500;text-transform:uppercase}
.hero .btn{left:113px;top:512px;width:210px;height:45px}
.play{position:absolute;left:1045px;top:570px;width:88px;height:88px;border-radius:50%;background:#fff;display:flex;align-items:center;justify-content:center}

.about{position:absolute;left:0;top:725px;width:1200px;height:807px;background:radial-gradient(ellipse 300px 420px at 1200px 0,#4a5aa0 0%,#4a2f6a 35%,transparent 75%),radial-gradient(ellipse 260px 360px at 0 807px,#7a3a7a 0%,#33204a 40%,transparent 75%),var(--bg)}
.about-art{position:absolute;left:105px;top:100px;width:460px;height:594px;border-radius:230px;background:radial-gradient(circle at 50% 45%,#9aa5f0,#8a6be0 45%,#c061c8 75%,transparent 78%)}
.section-h{font-size:46px}
.about-h{position:absolute;left:610px;top:125px}
.body-text{font-size:17px;line-height:30px}
.about-p{position:absolute;left:612px;top:198px;width:478px}
.mission-h{position:absolute;left:610px;top:438px;font-size:23px}
.mission-p{position:absolute;left:612px;top:480px;width:478px}
.about .btn{left:613px;top:628px;width:147px;height:45px}

.tech{position:absolute;left:0;top:1532px;width:1200px;height:721px;background:var(--bg)}
.center-h{position:absolute;left:0;width:1200px;text-align:center}
.tech-p{position:absolute;left:120px;top:183px;width:960px;text-align:center;font-size:17px;line-height:30px}
.feature{position:absolute;top:270px;width:300px;text-align:center}
.feature svg{display:block;margin:0 auto}
.feature h3{font-size:17px;font-weight:600;margin-top:14px}
.feature p{font-size:14.5px;line-height:26px;margin-top:16px}
.tech .btn{left:457px;top:549px;width:286px;height:45px}

.contact{position:absolute;left:0;top:2253px;width:1200px;height:620px;background:radial-gradient(ellipse 420px 520px at 1200px 0,#4a5aa0 0%,#4a2f6a 35%,transparent 75%),var(--bg)}
.field{position:absolute;background:var(--field);border:1px solid var(--field-line);padding:20px 26px;font-size:14px;text-transform:uppercase}
.contact .btn{left:526px;top:470px;width:147px;height:45px}

.footer{position:absolute;left:0;top:2873px;width:1200px;height:393px;background:var(--bg-deep)}
.rule{position:absolute;left:0;width:1200px;height:1px;background:var(--rule)}
.info{position:absolute;top:210px;font-size:16px;line-height:24px;font-weight:500;display:flex;gap:8px}
.copy{position:absolute;top:324px;left:0;width:1200px;text-align:center;font-size:12px;font-weight:500}
</style>
</head>
<body>

<section class="hero">
  <div class="hero-art abs" role="img" aria-label="Dark blue virus particles with glowing red spots" style="left:700px;top:90px;width:440px;height:430px;border-radius:50%;background:radial-gradient(circle at 55% 55%,#5a2a55,#2b3c72 55%,transparent 72%)"></div>
  <h1 class="hero-title display"><span class="lilac">Revolutionizing</span><br>T Cell Discovery for<br>Cancer &amp; Autoimmunity</h1>
  <p class="hero-sub">Introducing VORENT – a powerful, rapid, and cost-effective platform to identify antigen-specific T cells with unprecedented precision.</p>
  <a class="btn">How VORENT Works</a>
  <div class="play"><svg width="16" height="16" viewBox="0 0 16 16"><path d="M3 1l12 7-12 7z" fill="#000"/></svg></div>
</section>

<nav class="nav" style="top:0">
  <div class="brand"><span class="dot"></span>vorentbio</div>
  <div class="nav-links"><span class="active">Home</span><span>About Us</span><span>Technology</span></div>
  <a class="btn">Contact Us</a>
</nav>

<section class="about">
  <div class="about-art" role="img" aria-label="Molecular network of colourful cell-filled circles"></div>
  <h2 class="about-h section-h display"><span class="lilac">Who</span> We Are</h2>
  <p class="about-p body-text">VORENTbio is a healthcare technology startup developing breakthrough solutions in immune profiling. Our mission is to unlock the full potential of the immune system by enabling rapid and unbiased discovery of disease-specific T cells. Founded by scientists and innovators, we aim to transform how immune-based therapies are developed and delivered starting with our flagship platform: VORENT.</p>
  <h3 class="mission-h display lilac">Our Mission</h3>
  <p class="mission-p body-text">Our mission is to enable the rapid and unbiased identification of disease-specific T cells, unlocking new possibilities for diagnosing and treating cancer, autoimmune disorders, and infectious diseases.</p>
  <a class="btn">View More</a>
</section>

<section class="tech">
  <h2 class="center-h section-h display" style="top:100px"><span class="lilac">Our</span> Technology</h2>
  <p class="tech-p">VORENT is a next-generation screening technology designed to identify antigen-specific T cells quickly and accurately without the limitations of conventional methods.</p>
  <div class="feature" style="left:89px">
    <svg width="58" height="58" viewBox="0 0 58 58" fill="none" stroke="var(--icon)" stroke-width="2"><circle cx="29" cy="29" r="25" stroke-dasharray="6 4"/><circle cx="29" cy="29" r="16"/><path d="M31 19l-7 12h6l-3 9 8-13h-6z"/></svg>
    <h3>RAPID</h3>
    <p>Get actionable results in days — not weeks accelerating decision-making in research and clinical workflows.</p>
  </div>
  <div class="feature" style="left:447px">
    <svg width="72" height="62" viewBox="0 0 72 62" fill="none" stroke="var(--icon)" stroke-width="2"><path d="M4 16h16c14 0 20 30 34 30h10M4 46h16c14 0 20-30 34-30h10M58 8l8 8-8 8M58 38l8 8-8 8"/></svg>
    <h3>VERSATILE</h3>
    <p>A platform that works seamlessly across cancer, autoimmune, and infectious diseases — adaptable to a wide range of immune challenges.</p>
  </div>
  <div class="feature" style="left:807px">
    <svg width="62" height="62" viewBox="0 0 62 62" fill="none" stroke="var(--icon)" stroke-width="2"><path d="M31 6c-8 0-14 6-14 13s4 12 14 14c10-2 14-7 14-14S39 6 31 6zM31 6v27"/><path d="M4 28l8 22 10 8M58 28l-8 22-10 8"/></svg>
    <h3>UNBIASED</h3>
    <p>Screen entire antigen libraries without pre-selection bias — ensuring comprehensive and reliable immune profiling.</p>
  </div>
  <a class="btn">View More About Technology</a>
</section>

<section class="contact">
  <h2 class="center-h section-h display" style="top:74px"><span class="lilac">Contact</span> Us</h2>
  <div class="field" style="left:232px;top:170px;width:357px;height:57px">First Name</div>
  <div class="field" style="left:610px;top:170px;width:358px;height:57px">Last Name</div>
  <div class="field" style="left:232px;top:245px;width:357px;height:57px">Phone</div>
  <div class="field" style="left:610px;top:245px;width:358px;height:57px">Email Address</div>
  <div class="field" style="left:232px;top:321px;width:736px;height:124px">Message</div>
  <a class="btn">Submit</a>
</section>

<footer class="footer">
  <nav class="nav" style="top:0">
    <div class="brand" style="top:30px"><span class="dot"></span>vorentbio</div>
    <div class="nav-links" style="top:74px"><span class="active">Home</span><span>About Us</span><span>Technology</span></div>
    <a class="btn" style="top:61px">Contact Us</a>
  </nav>
  <div class="rule" style="top:160px"></div>
  <div class="info" style="left:112px"><svg width="12" height="16" viewBox="0 0 12 16"><path d="M6 0a6 6 0 00-6 6c0 4 6 10 6 10s6-6 6-10a6 6 0 00-6-6zm0 8a2 2 0 110-4 2 2 0 010 4z" fill="var(--icon)"/></svg><span>Based in [City, Country]<br>Advancing Immune Profiling Worldwide</span></div>
  <div class="info" style="left:594px;align-items:center"><svg width="16" height="12" viewBox="0 0 16 12"><rect width="16" height="12" fill="var(--icon)"/><path d="M0 0l8 6 8-6" stroke="var(--bg-deep)" fill="none"/></svg><span>info@vorentbio.com</span></div>
  <div class="info" style="left:1002px;align-items:center"><span style="width:12px;height:12px;background:var(--icon);display:inline-block"></span><span>Network</span></div>
  <div class="rule" style="top:280px"></div>
  <p class="copy">Copyright@2025.All Rights Reserved</p>
</footer>

</body>
</html>
```